Need Bold, Hip Card for Concert Ticket Website Gleaming Passes!

Hi there! I am putting together a business/website that sells event tickets (mostly concerts, but also some sports and theater). Think SeatNook, but much smaller. The site is called Gleaming Passes. I have a new logo (attached, with black/red/white color scheme), and am looking for a modern/cool/original business card design. Note that I am thinking of having the card itself in the shape of a ticket (die cut), so you may want to keep that in mind when designing, but I'm not set on that. I'm also open to alternative card sizes, thicknesses, glossy, spot UV, etc. in order to stand out. I'm attaching a potential die cut template and a sample card using that template in case you want to work with that.
Target Market(s)
Music fans, people that like going to see live events
Industry/Entity Type
Entertainment
Contact Information for Business Card
Information that I'd like to have:
website address - www.gleamingpasses.example
phone number: 1-833-5GLEAMNG (532-6264)
my name - Wendel Pike

```html
<!DOCTYPE html>
<html lang="en">
<head>
<meta charset="utf-8">
<title>Gleaming Passes – Business Card</title>
<link rel="stylesheet" href="https://fonts.googleapis.com/css2?family=Signika:wght@400;600;700&display=swap">
<style>
  :root {
    --backdrop: #8c6446;
    --ticket-red: #8b0306;
    --ticket-black: #0a0706;
    --panel-white: #ffffff;
    --ink-red: #8b0306;
    --ink-black: #0a0706;
  }
  * { margin: 0; padding: 0; box-sizing: border-box; }
  html, body {
    width: 1200px;
    height: 960px;
    overflow: hidden;
    background: var(--backdrop);
    font-family: "Signika", "Helvetica Neue", Arial, sans-serif;
  }
  .sheet {
    position: relative;
    width: 1200px;
    height: 960px;
  }
  .ticket-shapes {
    position: absolute;
    inset: 0;
  }
  .panel {
    position: absolute;
    left: 389px;
    width: 421px;
    height: 177px;
    display: flex;
    flex-direction: column;
    align-items: center;
    justify-content: center;
    text-align: center;
  }
  .panel--front { top: 229px; }
  .panel--back { top: 573px; }

  .brand {
    display: flex;
    align-items: center;
    gap: 16px;
  }
  .brand-mark {
    width: 44px;
    height: 44px;
    background: var(--ink-red);
  }
  .brand-name {
    color: var(--ink-red);
    font-weight: 700;
    font-size: 38px;
    line-height: 1;
    text-transform: uppercase;
    letter-spacing: 1px;
    text-align: left;
  }
  .brand-name span { display: block; }

  .holder-name {
    color: var(--ink-red);
    font-weight: 600;
    font-size: 23px;
    text-transform: uppercase;
    letter-spacing: 0.3px;
    margin-bottom: 10px;
  }
  .contact-list {
    list-style: none;
    color: var(--ink-red);
    font-size: 13px;
    line-height: 17px;
    text-transform: uppercase;
    letter-spacing: 0.3px;
  }
</style>
</head>
<body>
  <main class="sheet">
    <svg class="ticket-shapes" width="1200" height="960" viewBox="0 0 1200 960" aria-hidden="true">
      <!-- front ticket -->
      <path fill="var(--ticket-red)"
            d="M334,165 H866 V279 A37,37 0 0 0 866,353 V468 H334 V353 A37,37 0 0 0 334,279 Z"/>
      <rect x="389" y="229" width="421" height="177" fill="var(--panel-white)"/>
      <rect x="398" y="238" width="403" height="159" fill="none" stroke="var(--ticket-red)" stroke-width="4"/>

      <!-- back ticket -->
      <path fill="var(--ticket-black)"
            d="M334,509 H866 V624 A37,37 0 0 0 866,698 V813 H334 V698 A37,37 0 0 0 334,624 Z"/>
      <rect x="389" y="573" width="421" height="177" fill="var(--panel-white)"/>
      <rect x="398" y="582" width="403" height="159" fill="none" stroke="var(--ticket-black)" stroke-width="4"/>
    </svg>

    <section class="panel panel--front">
      <div class="brand">
        <div class="brand-mark"></div>
        <h1 class="brand-name"><span>Gleaming</span><span>Passes</span></h1>
      </div>
    </section>

    <section class="panel panel--back">
      <h2 class="holder-name">Wendel Pike</h2>
      <ul class="contact-list">
        <li>1-833-5GLEAMNG (532-6264)</li>
        <li>info@gleamingpasses.example</li>
        <li>www.gleamingpasses.example</li>
      </ul>
    </section>
  </main>
</body>
</html>
```